Poster Design For Obstacle Run

Design a poster for the Crow Ridge Obstacle run.
Text: Crow Ridge Obstacle Run. May 12th, 2018. Sittard. www.crowridgedash.nl. I have added a lot of pictures.
Furthermore, the logo should be included. As an example I included a poster from the ironbark race that we really like (ironbark team challenge) and also. Feel free to take a look at our website for inspiration: www.crowridgedash.nl

```html
<!DOCTYPE html>
<html lang="en">
<head>
<meta charset="utf-8">
<title>Crow Ridge Obstacle Run – Poster</title>
<link href="https://fonts.googleapis.com/css2?family=Bebas+Neue&family=Oswald:wght@400;500;600&family=Roboto+Slab:wght@700&display=swap" rel="stylesheet">
<style>
  :root {
    --orange: #e2572a;
    --orange-deep: #c8431c;
    --white: #f3f3f1;
    --mud: #5a3b2c;
    --slate: #6b6e72;
    --ink: #2a2624;
  }
  * { margin: 0; padding: 0; box-sizing: border-box; }
  html, body { width: 873px; height: 1200px; overflow: hidden; background: #e6e6e4; }
  .poster {
    position: relative;
    width: 873px;
    height: 1200px;
    overflow: hidden;
    background: var(--ink);
  }
  .poster__photo {
    position: absolute;
    inset: 0;
    background:
      linear-gradient(180deg, rgba(0,0,0,0) 70%, rgba(40,40,44,0.55) 100%),
      radial-gradient(ellipse 55% 45% at 88% 30%, #d8542c 0%, rgba(216,84,44,0.6) 45%, rgba(216,84,44,0) 75%),
      radial-gradient(ellipse 60% 30% at 50% 78%, #8a5a44 0%, rgba(110,70,52,0.7) 50%, rgba(0,0,0,0) 80%),
      linear-gradient(115deg, #9a9b96 0%, #7d7e7c 30%, #6a5a52 55%, #7a4a36 80%, #5a3b2c 100%);
  }
  .title {
    position: absolute;
    left: 0;
    width: 100%;
    text-align: center;
    font-family: "Bebas Neue", "Oswald", sans-serif;
    font-size: 176px;
    line-height: 1;
    color: var(--white);
    letter-spacing: 1px;
    text-shadow: 0 3px 8px rgba(0,0,0,0.25);
  }
  .title--top { top: 158px; }
  .title--bottom { top: 318px; }
  .title__accent { color: var(--orange); }
  .date-band {
    position: absolute;
    left: 203px;
    top: 527px;
    width: 474px;
    height: 72px;
    background: var(--orange);
    box-shadow: 0 4px 10px rgba(0,0,0,0.3);
    display: flex;
    align-items: center;
    justify-content: center;
    font-family: "Oswald", sans-serif;
    font-weight: 500;
    font-size: 38px;
    letter-spacing: 5px;
    color: var(--white);
  }
  .web-address {
    position: absolute;
    left: 0;
    width: 100%;
    top: 618px;
    text-align: center;
    font-family: "Roboto Slab", serif;
    font-weight: 700;
    font-size: 22px;
    color: var(--white);
    text-shadow: 0 2px 4px rgba(0,0,0,0.5);
  }
  .logo-art {
    position: absolute;
    left: 150px;
    top: 760px;
    width: 570px;
    height: 210px;
    border-radius: 40% 50% 45% 40%;
    background: radial-gradient(ellipse at 50% 50%, rgba(226,87,42,0.85) 0%, rgba(226,87,42,0.5) 55%, rgba(226,87,42,0) 80%);
  }
  .logo-meta {
    position: absolute;
    left: 241px;
    top: 928px;
    font-family: "Oswald", sans-serif;
    color: var(--white);
  }
  .logo-meta__city {
    display: block;
    font-size: 13px;
    letter-spacing: 7px;
    margin-bottom: 2px;
  }
  .logo-meta__date {
    display: inline-block;
    background: var(--white);
    color: var(--ink);
    font-size: 12px;
    font-weight: 500;
    letter-spacing: 1.5px;
    padding: 2px 9px;
  }
  .logo-name {
    position: absolute;
    left: 241px;
    top: 985px;
    width: 340px;
    font-family: "Oswald", sans-serif;
    font-weight: 500;
    font-size: 54px;
    line-height: 1.05;
    color: var(--white);
    text-transform: uppercase;
  }
</style>
</head>
<body>
  <main class="poster">
    <div class="poster__photo" role="img" aria-label="Close-up photo of a mud-covered runner in an orange shirt gripping a rope on a wooden obstacle wall"></div>

    <h1>
      <span class="title title--top">Crow Ridge</span>
      <span class="title title--bottom">Obstacle <span class="title__accent">Run</span></span>
    </h1>

    <div class="date-band">MAY 12TH, 2018</div>
    <p class="web-address">www.crowridgedash.nl</p>

    <div class="logo-art" role="img" aria-label="Illustration of two leaping runners over an orange paint splash"></div>
    <div class="logo-meta">
      <span class="logo-meta__city">SITTARD</span>
      <span class="logo-meta__date">MAY 12TH ,2018</span>
    </div>
    <p class="logo-name">Crow Ridge Obstacle Run</p>
  </main>
</body>
</html>
```